KestrelHollowCo.com

I need a site that I can sell dewatering equipment to the construction industry.
Ie, pipes fittings pumps and other such things needed to remove the groundwater on construction sites. Here in Florida, it’s needed almost everywhere seeing we are at sea level.
I want to be able to sell these products on the site and receive

```html
<!DOCTYPE html>
<html lang="en">
<head>
<meta charset="utf-8">
<title>Kestrel Hollow Co. — Dewatering Equipment</title>
<link href="https://fonts.googleapis.com/css2?family=Exo+2:wght@400;600;700&family=Lato:wght@400;700;900&display=swap" rel="stylesheet">
<style>
:root{
  --teal:#0a8fb5;
  --teal-light:#10a8c9;
  --teal-dark:#06729a;
  --navy:#0b5f86;
  --ink:#333;
  --muted:#555;
  --dark:#1d2228;
  --white:#fff;
  --star:#f2b705;
  --line:#dcdcdc;
}
*{box-sizing:border-box;margin:0;padding:0}
html,body{width:1200px;height:3766px;overflow:hidden}
body{font-family:"Lato",Arial,sans-serif;color:var(--ink);background:var(--white);position:relative}
.abs{position:absolute}
a{color:inherit;text-decoration:none}

/* header */
.site-header{position:absolute;top:0;left:0;width:1200px;height:115px;background:var(--white)}
.brand{position:absolute;left:78px;top:22px;display:flex;align-items:center;gap:14px}
.brand-dot{width:68px;height:68px;border-radius:50%;background:var(--teal)}
.brand-name{font-family:"Exo 2",sans-serif;font-weight:700;font-size:36px;color:var(--navy);line-height:1}
.brand-sub{font-family:"Exo 2",sans-serif;font-weight:700;font-size:36px;color:var(--navy)}
.head-contact{position:absolute;top:30px;display:flex;align-items:center;gap:14px}
.head-contact .ic{width:46px;height:46px;border-radius:50%;background:var(--teal);display:flex;align-items:center;justify-content:center}
.head-contact .lbl{font-size:15px;color:#333;text-transform:uppercase}
.head-contact .val{font-size:19px;color:var(--teal)}

/* nav */
.main-nav{position:absolute;top:115px;left:0;width:1200px;height:58px;background:linear-gradient(90deg,var(--teal-light),var(--navy))}
.main-nav ul{list-style:none;display:flex;position:absolute;left:80px;top:0;height:58px;align-items:center;gap:0}
.main-nav li{color:var(--white);font-weight:700;font-size:16px;margin-right:60px}
.quote-btn{position:absolute;right:78px;top:8px;height:42px;width:158px;border:2px solid var(--white);border-radius:21px;color:var(--white);font-weight:900;font-size:14px;display:flex;align-items:center;padding-left:14px}
.quote-btn::after{content:"";position:absolute;right:5px;top:5px;width:28px;height:28px;border-radius:50%;background:var(--white)}

/* hero */
.hero{position:absolute;top:173px;left:0;width:1200px;height:578px;background:linear-gradient(100deg,#2a3340 0%,#4a5b6b 35%,#6b5a44 65%,#3a2e26 100%)}
.hero-shade{position:absolute;inset:0;background:linear-gradient(90deg,rgba(10,20,30,.55),rgba(10,20,30,.05))}
.hero h1{position:absolute;left:78px;top:182px;font-family:"Lato",sans-serif;font-weight:900;font-size:41px;color:var(--white)}
.hero p{position:absolute;left:78px;top:248px;width:600px;font-size:15px;line-height:25px;color:var(--white)}
.pill-btn{position:absolute;height:52px;border:2px solid currentColor;border-radius:26px;font-weight:900;font-size:14px;display:flex;align-items:center;padding-left:18px}
.pill-btn::after{content:"";position:absolute;right:5px;top:5px;width:38px;height:38px;border-radius:50%;background:currentColor}
.hero .pill-btn{left:78px;top:334px;width:168px;color:var(--white)}
.hero-dots{position:absolute;left:560px;top:518px;display:flex;gap:12px}
.hero-dots span{width:14px;height:14px;border-radius:50%;background:rgba(255,255,255,.5)}
.hero-dots span.on{background:var(--white);box-shadow:0 0 0 3px rgba(255,255,255,.4)}

/* welcome */
.welcome-kicker{position:absolute;left:78px;top:812px;font-family:"Exo 2",sans-serif;font-size:38px;color:#444}
.welcome-title{position:absolute;left:78px;top:860px;font-family:"Exo 2",sans-serif;font-weight:700;font-size:46px;color:var(--navy)}
.welcome-text{position:absolute;left:78px;top:945px;width:590px;font-size:15px;line-height:26px;color:var(--muted)}
.welcome .pill-btn{left:78px;top:1104px;width:168px;color:var(--navy)}
.photo-ring{position:absolute;border-radius:50%;border:5px solid var(--white);box-shadow:0 0 0 3px var(--navy)}
.ring-a{left:740px;top:815px;width:228px;height:228px;background:radial-gradient(circle at 45% 50%,#b8313a,#5d6c5a 60%,#3f4a3c)}
.ring-b{left:886px;top:922px;width:232px;height:232px;background:radial-gradient(circle at 50% 55%,#d59a3a,#a77a4a 55%,#6d5a47)}

/* services */
.services{position:absolute;top:1222px;left:0;width:1200px;height:686px;background:linear-gradient(135deg,#16b1d0,#0a86ae 55%,#085e88)}
.sec-title{position:absolute;left:0;width:1200px;text-align:center;font-family:"Exo 2",sans-serif;font-size:40px}
.sec-title b{font-weight:700;font-size:46px}
.services .sec-title{top:55px;color:var(--white)}
.svc-card{position:absolute;width:322px;height:188px;background:var(--white);border-radius:4px;text-align:center;padding:72px 22px 0}
.svc-icon{position:absolute;left:115px;top:-44px;width:92px;height:92px;border-radius:50%;background:var(--white);border:3px solid var(--navy);box-shadow:0 0 0 5px var(--white);display:flex;align-items:center;justify-content:center}
.svc-card h3{font-size:18px;font-weight:700;color:var(--navy);margin-bottom:8px}
.svc-card p{font-size:14.5px;line-height:25px;color:var(--muted)}
.svc-card p a{color:var(--navy);font-weight:700;text-decoration:underline}

/* pumps */
.pumps .sec-title{top:1962px;color:var(--navy)}
.pumps-intro{position:absolute;left:280px;top:2052px;width:640px;text-align:center;font-size:15px;line-height:25px;color:var(--muted)}
.pump{position:absolute;top:2139px;width:234px}
.pump-img{width:234px;height:280px;border:2px solid var(--line);background:var(--white);display:flex;align-items:center;justify-content:center}
.pump.active .pump-img{border-color:var(--teal)}
.pump-img div{width:150px;height:190px;border-radius:30px}
.pump h4{margin-top:18px;font-size:18px;font-weight:700;color:var(--navy);padding-left:6px}
.pump .meta{display:flex;justify-content:space-between;padding:6px 40px 0 8px;font-size:14px;color:#666}
.stars{display:flex;gap:2px}
.stars i{width:10px;height:10px;background:var(--star);clip-path:polygon(50% 0,61% 38%,100% 38%,69% 60%,80% 100%,50% 76%,20% 100%,31% 60%,0 38%,39% 38%)}
.stars i.off{background:#ccc}
.buy-btn{display:block;margin:22px auto 0;width:108px;height:40px;border-radius:20px;background:var(--navy);color:var(--white);font-size:13px;font-weight:900;text-align:center;line-height:40px}
.pump.active .buy-btn{background:var(--white);color:var(--navy);border:2px solid var(--navy);line-height:36px}

/* projects */
.projects{position:absolute;top:2617px;left:0;width:1200px;height:594px;background:linear-gradient(180deg,#15191e,#2a3038)}
.projects .sec-title{top:52px;color:var(--white)}
.proj{position:absolute;border:1px solid rgba(255,255,255,.15)}
.view-overlay{position:absolute;left:0;right:0;top:55px;height:78px;background:rgba(10,143,181,.85);color:var(--white);font-weight:700;font-size:18px;text-align:center;padding-top:42px}
.view-overlay::before{content:"";position:absolute;left:50%;top:12px;width:24px;height:14px;margin-left:-12px;border:2px solid var(--white);border-radius:50%}

/* contact strip */
.contact-item{position:absolute;top:3272px;display:flex;gap:16px}
.contact-item .ic{width:50px;height:50px;border-radius:50%;background:var(--teal);display:flex;align-items:center;justify-content:center;flex:none}
.contact-item h5{font-size:17px;font-weight:700;color:var(--teal);margin-bottom:4px}
.contact-item p{font-size:14.5px;line-height:24px;color:var(--muted)}

/* footer */
.site-footer{position:absolute;top:3410px;left:0;width:1200px;height:356px;background:linear-gradient(135deg,#14aece,#0a84ad 55%,#075b86);color:var(--white)}
.foot-brand{position:absolute;left:0;width:1200px;top:44px;display:flex;justify-content:center;align-items:center;gap:14px}
.foot-brand .brand-dot{background:var(--white);width:60px;height:60px}
.foot-brand .brand-name{color:var(--white);font-size:32px}
.foot-nav{position:absolute;top:152px;left:0;width:1200px;text-align:center;font-size:16px;font-weight:700}
.foot-nav span{margin:0 14px}
.social{position:absolute;top:218px;left:0;width:1200px;display:flex;justify-content:center;gap:16px}
.social i{width:40px;height:40px;border-radius:50%;background:var(--white)}
.foot-line{position:absolute;top:292px;left:78px;width:1044px;height:1px;background:rgba(255,255,255,.5)}
.copyright{position:absolute;top:314px;left:0;width:1200px;text-align:center;font-size:14px}
</style>
</head>
<body>

<header class="site-header">
  <div class="brand"><span class="brand-dot"></span><span class="brand-name">Kestrel Hollow Co.</span></div>
  <div class="head-contact" style="left:672px">
    <span class="ic"><svg width="22" height="22" viewBox="0 0 24 24"><path fill="#fff" d="M6.6 10.8a15 15 0 0 0 6.6 6.6l2.2-2.2a1 1 0 0 1 1-.25 11.4 11.4 0 0 0 3.6.57 1 1 0 0 1 1 1V20a1 1 0 0 1-1 1A17 17 0 0 1 3 4a1 1 0 0 1 1-1h3.5a1 1 0 0 1 1 1c0 1.25.2 2.45.57 3.57a1 1 0 0 1-.25 1z"/></svg></span>
    <div><div class="lbl">Call Us</div><div class="val">123-456-7890</div></div>
  </div>
  <div class="head-contact" style="left:888px">
    <span class="ic"><svg width="22" height="22" viewBox="0 0 24 24"><path fill="#fff" d="M3 5h18v14H3z"/><path d="M3 6l9 7 9-7" stroke="#0a8fb5" stroke-width="2" fill="none"/></svg></span>
    <div><div class="lbl" style="text-transform:none">E-mail</div><div class="val">info@kestrelhollowco.com</div></div>
  </div>
</header>

<nav class="main-nav">
  <ul><li>Home</li><li>About Us</li><li>Pumps</li><li>Services</li><li>Projects</li><li>Contact Us</li></ul>
  <a class="quote-btn">GET A QUOTE</a>
</nav>

<section class="hero" role="img" aria-label="Crane barge working on a waterfront construction site at dusk">
  <div class="hero-shade"></div>
  <h1>KESTREL HOLLOW Co.</h1>
  <p>Lorem Ipsum is simply dummy text of the printing and typesetting industry. Lorem Ipsum has been the industry's standard dummy text ever since the 1500s.</p>
  <a class="pill-btn">CONTACT US</a>
  <div class="hero-dots"><span></span><span class="on"></span><span></span></div>
</section>

<section class="welcome">
  <div class="welcome-kicker">Welcome To</div>
  <h2 class="welcome-title">Kestrel Hollow Co.</h2>
  <p class="welcome-text">Lorem Ipsum is simply dummy text of the printing and typesetting industry. Lorem Ipsum has been the industry's standard dummy text ever since the 1500s, when an unknown printer took a galley of type and scrambled it to make a type specimen book. It has survived not only five centuries, but also the leap into electronic typesetting, remaining essentially unchanged.</p>
  <a class="pill-btn">LEARN MORE</a>
  <div class="photo-ring ring-a" role="img" aria-label="Red dewatering pump on a skid at a job site"></div>
  <div class="photo-ring ring-b" role="img" aria-label="Excavator digging a trench on a sandy site"></div>
</section>

<section class="services">
  <h2 class="sec-title">Our <b>Services</b></h2>
  <div class="svc-card" style="left:78px;top:176px"><span class="svc-icon"><svg width="44" height="44" viewBox="0 0 44 44" fill="none" stroke="#0b5f86" stroke-width="3"><circle cx="22" cy="24" r="12"/><path d="M22 24l8-6M8 36h28"/></svg></span><h3>Pumping Services</h3><p>Lorem Ipsum is simply dummy text of the printing and typesetting industry. Lorem Ipsum has been the...<a>Read More »</a></p></div>
  <div class="svc-card" style="left:439px;top:176px"><span class="svc-icon"><svg width="44" height="44" viewBox="0 0 44 44" fill="none" stroke="#0b5f86" stroke-width="3"><rect x="8" y="8" width="28" height="28" rx="3"/><path d="M14 18h16M14 26h16"/></svg></span><h3>Dewatering</h3><p>Lorem Ipsum is simply dummy text of the printing and typesetting industry. Lorem Ipsum has been the...<a>Read More »</a></p></div>
  <div class="svc-card" style="left:800px;top:176px"><span class="svc-icon"><svg width="44" height="44" viewBox="0 0 44 44" fill="none" stroke="#0b5f86" stroke-width="3"><path d="M6 34h32M10 34v-8h14v8M24 28l6-14 8 6"/></svg></span><h3>One-Pass Trenching</h3><p>Lorem Ipsum is simply dummy text of the printing and typesetting industry. Lorem Ipsum has been the...<a>Read More »</a></p></div>
  <div class="svc-card" style="left:78px;top:435px"><span class="svc-icon"><svg width="44" height="44" viewBox="0 0 44 44" fill="none" stroke="#0b5f86" stroke-width="3"><path d="M22 6v32M12 38l10-32 10 32M10 16h24M12 24h20"/></svg></span><h3>Power Generation</h3><p>Lorem Ipsum is simply dummy text of the printing and typesetting industry. Lorem Ipsum has been the...<a>Read More »</a></p></div>
  <div class="svc-card" style="left:439px;top:435px"><span class="svc-icon"><svg width="44" height="44" viewBox="0 0 44 44" fill="none" stroke="#0b5f86" stroke-width="3"><path d="M22 10c-5 7-8 11-8 15a8 8 0 0 0 16 0c0-4-3-8-8-15z"/><path d="M8 22a14 14 0 0 1 6-11M36 22a14 14 0 0 1-6 11"/></svg></span><h3>Water Filtration &amp; Treatmet</h3><p>Lorem Ipsum is simply dummy text of the printing and typesetting industry. Lorem Ipsum has been the...<a>Read More »</a></p></div>
  <div class="svc-card" style="left:800px;top:435px"><span class="svc-icon"><svg width="44" height="44" viewBox="0 0 44 44" fill="none" stroke="#0b5f86" stroke-width="3"><path d="M16 6v24M12 6h8M8 38h28M16 30l-4 8M16 30l4 8M26 38V24h8v14"/></svg></span><h3>Drilling</h3><p>Lorem Ipsum is simply dummy text of the printing and typesetting industry. Lorem Ipsum has been the...<a>Read More »</a></p></div>
</section>

<section class="pumps">
  <h2 class="sec-title"><b>Pumps</b></h2>
  <p class="pumps-intro">Lorem Ipsum is simply dummy text of the printing and typesetting industry. Lorem Ipsum has been the industry's standard dummy text ever since the 1500s.</p>
  <div class="pump" style="left:78px"><div class="pump-img"><div role="img" aria-label="White double diaphragm pump" style="background:linear-gradient(160deg,#f1f1f1,#c9c9c9)"></div></div><h4>Double Diaphragm Pumps</h4><div class="meta"><span>$90.00</span><span class="stars"><i></i><i></i><i></i><i class="off"></i><i class="off"></i></span></div><a class="buy-btn">BUY NOW</a></div>
  <div class="pump active" style="left:347px"><div class="pump-img"><div role="img" aria-label="Stainless steel rotary lobe pump" style="background:linear-gradient(160deg,#e6e8ea,#8d9399)"></div></div><h4>Rotary Lobe Pumps</h4><div class="meta"><span>$90.00</span><span class="stars"><i></i><i></i><i></i><i class="off"></i><i class="off"></i></span></div><a class="buy-btn">BUY NOW</a></div>
  <div class="pump" style="left:617px"><div class="pump-img"><div role="img" aria-label="Teal vertical jet pump with motor" style="background:linear-gradient(160deg,#4fb7c4,#1f7482)"></div></div><h4>Jet Pumps</h4><div class="meta"><span>$90.00</span><span class="stars"><i></i><i></i><i></i><i class="off"></i><i class="off"></i></span></div><a class="buy-btn">BUY NOW</a></div>
  <div class="pump" style="left:888px"><div class="pump-img"><div role="img" aria-label="Orange centrifugal pump" style="background:linear-gradient(160deg,#f49a4a,#d96a1c)"></div></div><h4>Harlow Pumps</h4><div class="meta"><span>$90.00</span><span class="stars"><i></i><i></i><i></i><i class="off"></i><i class="off"></i></span></div><a class="buy-btn">BUY NOW</a></div>
</section>

<section class="projects">
  <h2 class="sec-title">Our <b>Projects</b></h2>
  <div class="proj" style="left:78px;top:147px;width:520px;height:186px;background:linear-gradient(120deg,#6a5a48,#b98a3a 50%,#3d4a58)" role="img" aria-label="Large dewatering pipes on a project site"><div class="view-overlay">View Project</div></div>
  <div class="proj" style="left:603px;top:147px;width:258px;height:186px;background:linear-gradient(160deg,#4e86b8,#c9b44a 60%,#6b6e70)" role="img" aria-label="Workers on an industrial platform"></div>
  <div class="proj" style="left:866px;top:147px;width:256px;height:186px;background:linear-gradient(160deg,#b38458,#d6a770 55%,#8a6a4a)" role="img" aria-label="Excavator on a dirt site"></div>
  <div class="proj" style="left:78px;top:338px;width:256px;height:188px;background:linear-gradient(160deg,#8d9aa6,#a2603e 55%,#4f5a66)" role="img" aria-label="Container port from above"></div>
  <div class="proj" style="left:339px;top:338px;width:259px;height:188px;background:linear-gradient(160deg,#6f8a5a,#b3302f 55%,#5a4a3a)" role="img" aria-label="Red pump trailer on site"></div>
  <div class="proj" style="left:603px;top:338px;width:519px;height:188px;background:linear-gradient(160deg,#8fb4d6,#d8dde2 45%,#6a6254)" role="img" aria-label="Drilling rig spraying water"></div>
</section>

<section class="contact-strip">
  <div class="contact-item" style="left:78px"><span class="ic"><svg width="22" height="22" viewBox="0 0 24 24"><path fill="#fff" d="M12 2a7 7 0 0 0-7 7c0 5 7 13 7 13s7-8 7-13a7 7 0 0 0-7-7zm0 9.5A2.5 2.5 0 1 1 12 6.5a2.5 2.5 0 0 1 0 5z"/></svg></span><div><h5>Address</h5><p>123, Lorem Ipsum is simply dummy<br>text of the typesetting industry.</p></div></div>
  <div class="contact-item" style="left:439px"><span class="ic"><svg width="22" height="22" viewBox="0 0 24 24"><path fill="#fff" d="M6.6 10.8a15 15 0 0 0 6.6 6.6l2.2-2.2a1 1 0 0 1 1-.25 11.4 11.4 0 0 0 3.6.57 1 1 0 0 1 1 1V20a1 1 0 0 1-1 1A17 17 0 0 1 3 4a1 1 0 0 1 1-1h3.5a1 1 0 0 1 1 1c0 1.25.2 2.45.57 3.57a1 1 0 0 1-.25 1z"/></svg></span><div><h5>Call Us</h5><p>123-456-7890</p></div></div>
  <div class="contact-item" style="left:800px"><span class="ic"><svg width="22" height="22" viewBox="0 0 24 24"><path fill="#fff" d="M3 5h18v14H3z"/><path d="M3 6l9 7 9-7" stroke="#0a8fb5" stroke-width="2" fill="none"/></svg></span><div><h5>E-mail</h5><p>info@kestrelhollowco.com</p></div></div>
</section>

<footer class="site-footer">
  <div class="foot-brand"><span class="brand-dot"></span><span class="brand-name">Kestrel Hollow Co.</span></div>
  <div class="foot-nav"><span>Home</span>|<span>About Us</span>|<span>Pumps</span>|<span>Services</span>|<span>Projects</span>|<span>Contact Us</span></div>
  <div class="social"><i></i><i></i><i></i><i></i></div>
  <div class="foot-line"></div>
  <div class="copyright">© KESTREL HOLLOW CO. - 2018. All Rights Reserved.</div>
</footer>

</body>
</html>
```